Calm Harbor Blueprint

I need a on page electronic flyer for this coaching program. I want a silhouette to accompany the case the copy starts with. I have the copy written but need it put together in a striking way.

Target Market(s)

towards higher net worth individuals

Industry/Entity Type

Electronic

```html
<!DOCTYPE html>
<html lang="en">
<head>
<meta charset="utf-8">
<title>Calm Harbor Blueprint – Coaching Flyer</title>
<link href="https://fonts.googleapis.com/css2?family=Oswald:wght@600;700&family=Arimo:ital,wght@0,400;0,700;1,400;1,700&display=swap" rel="stylesheet">
<style>
  :root {
    --field-green: #6fb844;
    --headline-orange: #f9a51e;
    --headline-shadow: rgba(0,0,0,0.45);
    --heading-red: #d52b1e;
    --heading-blue: #1c6db4;
    --panel-white: #ffffff;
    --panel-edge: #2a2a2a;
    --ink: #222222;
    --silhouette: #1b1b1b;
    --white: #ffffff;
  }
  * { margin: 0; padding: 0; box-sizing: border-box; }
  html, body { width: 1200px; height: 927px; overflow: hidden; }
  body { background: #ffffff; }
  .flyer {
    position: relative;
    width: 1200px; height: 927px;
    background: var(--field-green);
    overflow: hidden;
    font-family: "Arimo", Arial, sans-serif;
    color: var(--ink);
  }

  /* Case-study silhouette */
  .case-silhouette {
    position: absolute; left: 94px; top: 0; width: 194px; height: 303px;
    background: linear-gradient(180deg, #2a2a2a 0%, var(--silhouette) 100%);
    border-radius: 80px 80px 0 0;
  }
  .case-caption {
    position: absolute; left: 103px; top: 277px;
    font-size: 10px; color: var(--white);
  }

  /* Headline */
  .headline { position: absolute; left: 0; top: 0; width: 1200px; font-weight: 400; }
  .headline__lead, .headline__about {
    position: absolute; white-space: nowrap;
    font-family: "Arimo", Arial, sans-serif;
    font-style: italic; color: var(--white);
    text-shadow: 2px 2px 3px var(--headline-shadow);
    line-height: 1;
  }
  .headline__lead { left: 292px; top: 44px; font-size: 60px; }
  .headline__about { left: 505px; top: 236px; font-size: 52px; }
  .headline__big {
    position: absolute; white-space: nowrap;
    font-family: "Oswald", "Arial Narrow", sans-serif;
    font-weight: 700; color: var(--headline-orange);
    text-transform: uppercase;
    text-shadow: 3px 3px 4px var(--headline-shadow);
    line-height: 1;
  }
  .headline__big--advice { left: 290px; top: 109px; font-size: 90px; }
  .headline__big--numbers { left: 652px; top: 199px; font-size: 96px; }

  /* White content panel */
  .panel {
    position: absolute; left: 61px; top: 303px; width: 1124px; height: 495px;
    background: var(--panel-white);
    border: 3px solid var(--panel-edge);
    border-radius: 18px;
  }
  .story, .program { position: absolute; top: 18px; }
  .story { left: 16px; width: 518px; }
  .program { left: 557px; width: 545px; }

  .story__title, .program__title {
    font-family: "Arimo", Arial, sans-serif; font-weight: 400;
    text-transform: uppercase; font-size: 27px; line-height: 1.05;
  }
  .story__title { color: var(--heading-red); }
  .program__title { color: var(--heading-blue); }
  .story__subtitle, .program__subtitle {
    font-weight: 400; font-size: 21px; line-height: 1.15; margin-bottom: 18px;
  }
  .story__subtitle { color: var(--heading-red); }
  .program__subtitle { color: var(--heading-blue); font-size: 20px; }

  .copy { font-size: 12.4px; line-height: 1.42; margin-bottom: 14px; }
  .program__intro { font-size: 15px; margin-bottom: 6px; }
  .program__list { list-style: none; margin-bottom: 16px; }
  .program__list li {
    font-size: 12.4px; line-height: 1.45; padding-left: 12px; position: relative;
  }
  .program__list li::before {
    content: ""; position: absolute; left: 0; top: 6px;
    width: 6px; height: 6px; border-radius: 50%; background: var(--heading-blue);
  }
  .copy--narrow { width: 215px; }

  .story__divider {
    position: absolute; left: 16px; top: 384px; width: 518px;
    border: 0; border-top: 1px solid #999;
  }
  .author-bio {
    position: absolute; left: 16px; top: 420px; width: 530px;
    font-size: 11.8px; line-height: 1.45; font-style: italic;
  }
  .author-bio strong { font-weight: 700; }

  /* Client photo */
  .client-photo {
    position: absolute; left: 860px; top: 636px; width: 340px; height: 291px;
    background: linear-gradient(135deg, #e6a98d 0%, #c97c63 45%, #3b4f8f 75%, #23346a 100%);
    border-radius: 110px 0 0 0;
    z-index: 2;
  }

  /* Footer */
  .contact { position: absolute; left: 0; top: 0; z-index: 3; }
  .brand { position: absolute; left: 30px; top: 840px; display: flex; align-items: center; gap: 8px; }
  .brand__dot { width: 40px; height: 40px; border-radius: 50%; background: var(--heading-blue); }
  .brand__name {
    font-family: "Arimo", Arial, sans-serif; font-weight: 700; font-size: 14px; color: var(--white);
    width: 100px; line-height: 1.1;
  }
  .contact__lead {
    position: absolute; left: 186px; top: 830px; white-space: nowrap;
    font-style: italic; font-size: 24px; color: var(--white);
    text-shadow: 1px 1px 2px var(--headline-shadow);
  }
  .contact__line {
    position: absolute; left: 186px; top: 854px;
    font-family: "Oswald", "Arial Narrow", sans-serif; font-weight: 700;
    font-size: 42px; line-height: 1.2; color: var(--headline-orange);
    text-shadow: 2px 2px 3px var(--headline-shadow);
    white-space: nowrap;
  }
  .contact__sep { margin: 0 10px; }
</style>
</head>
<body>
<div class="flyer">

  <div class="case-silhouette" role="img" aria-label="Black silhouette of a man's head and shoulders representing the case study client"></div>
  <p class="case-caption">“Daniel” Riverton, PA</p>

  <h1 class="headline">
    <span class="headline__lead">Sometimes the best</span>
    <span class="headline__big headline__big--advice">Financial advice isn’t</span>
    <span class="headline__about">about</span>
    <span class="headline__big headline__big--numbers">Numbers...</span>
  </h1>

  <section class="panel">
    <article class="story">
      <h2 class="story__title">Calm Harbor Blueprint:</h2>
      <p class="story__subtitle">From Financial Worries to Wealth Satisfaction</p>
      <p class="copy">A 49 year old attorney, Daniel was used to success and rising net worth. But with huge losses in the market crash, layoffs at his firm, his kids heading for college and the stagnant economy stretching ahead, his usual optimism is gone.</p>
      <p class="copy">With his anxiety growing, Daniel doubts his own decision making ability. His confidence slipping, he stopped opening his financial statements and could barely speak to his financial advisor. He thought if his advisor said “hang in there” one more time, he just might blow up.</p>
      <p class="copy">Yet Daniel felt too embarrassed to talk about his deep worries, even with his wife. It seemed like all he could do was pour another glass of wine and suffer in isolation.</p>
      <p class="copy">If you’re like Daniel, you’re afraid and alone with plenty of company. In a September 2009 National Counseling Society poll, 80 percent reported the economy is causing significant stress, up from 66 percent from the previous April. The Restful Nights Institute said 27 percent of people surveyed had sleeplessness because of economic anxiety.</p>
    </article>
    <hr class="story__divider">
    <p class="author-bio"><strong>Alan Mercer, Ph.D. is a psychologist with 30 years of experience treating anxiety and stress. He is co-founder and facilitator of Harborline Circle, a peer learning group for high net worth investors.</strong></p>

    <article class="program">
      <h2 class="program__title">How can you take control</h2>
      <p class="program__subtitle">of these worries and get back to enjoying your life?</p>
      <p class="program__intro">In this 5 session coaching process you will:</p>
      <ul class="program__list">
        <li>Learn a decision making tool to make choices that truly serve your needs</li>
        <li>Clarify and more fully engage with your purpose and passions</li>
        <li>Improve your relationship with your financial advisor</li>
        <li>Feel more in control and confident in your financial life</li>
      </ul>
      <p class="copy">This process guides you to step back and understand the source of your financial worry your unique story about the meaning of money. Your money story drives your emotions and decision making—for better and worse. You’ll learn a decision making tool for more conscious, effective and satisfying financial and life decisions.</p>
      <p class="copy copy--narrow">You’ll also examine your core values and strengths—what really matters most to you and how you work at your best. When you use your money and your core strengths to pursue your highest aspirations, life and wealth become balanced. As you commit more fully to your mission and passions, satisfaction grows and money worries melt away.</p>
    </article>
  </section>

  <div class="client-photo" role="img" aria-label="Photo of a startled man in a suit and striped tie leaning into the frame"></div>

  <footer class="contact">
    <div class="brand">
      <span class="brand__dot"></span>
      <span class="brand__name">Harborline Circle</span>
    </div>
    <p class="contact__lead">For more information, call</p>
    <p class="contact__line">555-014-0422<span class="contact__sep">|</span>amercer@example.com</p>
  </footer>

</div>
</body>
</html>
```